Candle company needs a label for candle

Looking for a designer to create my candle label. I am going to attach a few pictures of my vision for the label as well as my Company Logo and jar I have puchased. I'm going for the modern rustic feel but you are the designer and have full trust in your abilities. The label is going to be printed on Kraft paper (2x3) so looking for the font to be black. The candle label MUST include the following information:
Candle Birchway Co.
NO. 01: Eucalyptus + Spearmint
Handmade In NJ
Soy Wax
9oz

Industry/Entity Type

Candle Industry

Colors

Designer to choose colors to be used in the design.

Requirements
Should not have
• Any images

```html
<!DOCTYPE html>
<html lang="en">
<head>
<meta charset="utf-8">
<title>Candle Birchway Co. — No. 01 Label</title>
<link href="https://fonts.googleapis.com/css2?family=Jost:wght@300;400;500;600&display=swap" rel="stylesheet">
<style>
  :root {
    --backdrop: #b7b7b7;
    --paper: #ffffff;
    --ink: #333333;
    --ink-deep: #1f1f1f;
    --pattern: #efefef;
  }
  html, body {
    margin: 0;
    padding: 0;
    width: 1200px;
    height: 1136px;
    overflow: hidden;
    background: var(--backdrop);
  }
  .canvas {
    position: relative;
    width: 1200px;
    height: 1136px;
    background: var(--backdrop);
  }
  .label {
    position: absolute;
    left: 255px;
    top: 232px;
    width: 690px;
    height: 670px;
    background: var(--paper);
    box-shadow: 6px 8px 22px rgba(0, 0, 0, 0.35);
    overflow: hidden;
    font-family: "Jost", sans-serif;
    color: var(--ink);
  }
  .pattern {
    position: absolute;
  }
  .pattern--top-left {
    left: 0; top: 0; width: 200px; height: 210px;
    background: radial-gradient(ellipse at top left, var(--pattern) 0%, rgba(239,239,239,0) 75%);
  }
  .pattern--right {
    right: 0; top: 120px; width: 120px; height: 370px;
    background: radial-gradient(ellipse at right center, var(--pattern) 0%, rgba(239,239,239,0) 70%);
  }
  .pattern--bottom-left {
    left: 0; bottom: 0; width: 290px; height: 275px;
    background: radial-gradient(ellipse at bottom left, var(--pattern) 0%, rgba(239,239,239,0) 75%);
  }
  .pattern--bottom-right {
    right: 0; bottom: 0; width: 280px; height: 110px;
    background: radial-gradient(ellipse at bottom right, var(--pattern) 0%, rgba(239,239,239,0) 75%);
  }
  .brand-name {
    position: absolute;
    left: 0; right: 0;
    top: 112px;
    margin: 0;
    text-align: center;
    font-weight: 500;
    font-size: 46px;
    line-height: 54px;
    letter-spacing: 0;
    color: var(--ink);
  }
  .scent {
    position: absolute;
    left: 0; right: 0;
    top: 314px;
    margin: 0;
    text-align: center;
    font-weight: 500;
    font-size: 43px;
    line-height: 48px;
    color: var(--ink);
  }
  .origin {
    position: absolute;
    left: 0; right: 0;
    top: 418px;
    margin: 0;
    text-align: center;
    font-weight: 300;
    font-size: 50px;
    line-height: 54px;
    color: var(--ink-deep);
  }
  .origin strong { font-weight: 600; }
  .wax-badge {
    position: absolute;
    left: 228px;
    top: 487px;
    width: 229px;
    height: 62px;
    border: 2px solid var(--ink);
    display: flex;
    align-items: center;
    justify-content: center;
    font-weight: 500;
    font-size: 48px;
    color: var(--ink-deep);
  }
  .net-weight {
    position: absolute;
    left: 0; right: 0;
    top: 586px;
    height: 48px;
  }
  .net-weight__rule {
    position: absolute;
    top: 23px;
    height: 2px;
    background: var(--ink);
  }
  .net-weight__rule--left { left: 0; width: 298px; }
  .net-weight__rule--right { left: 387px; right: 0; }
  .net-weight__value {
    position: absolute;
    left: 298px;
    width: 89px;
    top: 0;
    text-align: center;
    font-weight: 500;
    font-size: 40px;
    line-height: 48px;
    color: var(--ink-deep);
  }
</style>
</head>
<body>
<div class="canvas">
  <section class="label">
    <div class="pattern pattern--top-left" role="img" aria-label="Faint geometric cube pattern"></div>
    <div class="pattern pattern--right" role="img" aria-label="Faint geometric cube pattern"></div>
    <div class="pattern pattern--bottom-left" role="img" aria-label="Faint geometric cube pattern"></div>
    <div class="pattern pattern--bottom-right" role="img" aria-label="Faint geometric cube pattern"></div>

    <h1 class="brand-name">Candle Birchway Co.</h1>

    <p class="scent">NO. 01:<br>Eucalyptus + Spearmint</p>
    <p class="origin">Handmade In <strong>NJ</strong></p>
    <div class="wax-badge">Soy Wax</div>

    <div class="net-weight">
      <span class="net-weight__rule net-weight__rule--left"></span>
      <span class="net-weight__value">9oz</span>
      <span class="net-weight__rule net-weight__rule--right"></span>
    </div>
  </section>
</div>
</body>
</html>
```